Fable Organics Label Project- Updates made to project!

Project Scope: Branding opportunity for internet based skin care line. Design coordinating label for 4 different products. Each design shall be editable in Adobe Illustrator as a template including all fonts, symbols, and guides. Submit a design for all 4 products (preferably together as it would look on a retail shelf), business card, and logo.
Cleanser: STEP 1 Label Size: 5 x 4.5 inches (w x h) LULL CLEANSER
Toner: STEP 2 Label Size: 5 x 4.5 inches (w x h) HUSHWAY TONER- A piece of each crystal sits at the bottom of each solution. It coordinates with the "Calm Within" of our logo.
Serum STEP 3 Label Size: Label Size: 4.25 x 2.25 ANTI-AGING SERUM
Moisturizer: STEP 4 Label Size: Label Size: 1”x7.25” MOISTURIZER
Each label needs to include:
Front:
Attractive larger sized STEP #
Logo
Product name and short description
Decorative design Symbol(s)
Back:
Area on back to say short description
Directions for use
Larger area for ingredients
Website: www.fableorganics-example.com
Address of distribution
Barcode

Fable Skin Care, an esthetician created line provides organic and natural based products for all skin types. With an emphasis on anti-aging, this simple 4- step system can be used by many including pregnant and oncology consumers. The unique thing about our line is that the toners and serums contain crystals such as amethyst and rose quarts to promote inner peace as well as outer beauty. Each product is handmade with natural, quality ingredients and are 70-90% Organic.
Target Market: Women ages 30-45 years old. This demographic is on the go, and wants a simple-easy to read label, & a skin care system that addresses her concerns. Just as this consumer is mindful of her fitness and what she puts in her body, she tends to purchase environmentally friendly, and natural products. Health and wellness trends reflect this, as organic beauty products are expected to grow 74% from 2013 to 2018. She enjoys meditation and yoga, and she is curious about eastern medicine holistic healing trends.

Company Name: Fable Skin Care
Tagline: Calm Within- Glow Without
Package Feel: Simple, elegant easy to read step on each product. STEP 1: AM/PM. Attractive numbering. A symbol that reflects the brand. Not necessarily a Fable or Crystal because the name speaks for itself. Beautiful, soft, eye catching design that draws the consumer to pick it up. Clear or white label welcomed. Some color palettes provided.
Descriptive words the packaging should represent: Yoga, Zen, mystic, eye catching, healing energy, natural, quality ingredients, sophisticated, beautiful, serenity, easy to read- bold-attractive numbering on front.
Inspiration Brands: KAVU Organics- Beautiful watercolor packaging that resonates a "feeling"

Attached are pictures of the packaging, inspirational pictures, skin care lines that are attractive, ect.

Packaging SPECS:

Cleanser:
Color Clear
Size 4 oz
Material PET
Case Pack
Neck Finish 24-410
Diameter 1.58 in / 4.013 cm
Height 6 in / 15.240 cm
Label Dimensions 5x4.5
Print Dimensions 5x4.5
Print Dimensions in (diameter)

TONER BOTTLE: Same as above

SERUM BOTTLE:
Color Clear
Size 2 oz
Material PET
Neck Finish 20-410
Diameter 1.358 in / 3.449 cm
Height 3.274 in / 8.316 cm

Moisturizer:
2.3 oz
Height:53 mm
Diameter: 60 mm
Neck: 58/400

Target Market(s)

Women ages 30-45 years old. This demographic is on the go, and wants a simple-easy to read label, & a skin care system that addresses her concerns. Just as this consumer is mindful of her fitness and what she puts in her body, she tends to purchase environmentally friendly, and natural products. Health and wellness trends reflect this, as organic beauty products are expected to grow 74% from 2013 to 2018. She enjoys meditation and yoga, and she is curious about eastern medicine holistic healing trends.

Industry/Entity Type

Skin Care Product

Contact Information for Business Card

Details given upon completion.

Logo Text

Fable Organics Calm Within- Glow Without

Requirements
Must have
• A large step number on the front. Coordinating symbols and colors. Must have a professional retail look and be easy to read.
Nice to have
• Clean, simple, eye catching packaging. Watercolor designs. Designs that inspire "feelings" www.kavuorganics-example.com

```html
<!DOCTYPE html>
<html lang="en">
<head>
<meta charset="UTF-8">
<title>Fable Skin Care – Business Card</title>
<link href="https://fonts.googleapis.com/css2?family=Open+Sans:wght@300;400;700;800&family=Kaushan+Script&display=swap" rel="stylesheet">
<style>
  :root {
    --page: #ffffff;
    --card-light: #ffffff;
    --card-dark: #000000;
    --ink: #111111;
    --paper-text: #ffffff;
    --soft-text: #e6e6e6;
    --edge: #e4e0d6;
  }
  * { margin: 0; padding: 0; box-sizing: border-box; }
  html, body {
    width: 1200px;
    height: 848px;
    overflow: hidden;
    background: var(--page);
  }
  .sheet {
    position: relative;
    width: 1200px;
    height: 848px;
  }
  .card {
    position: absolute;
    left: 300px;
    width: 600px;
    height: 332px;
  }
  .card--front {
    top: 72px;
    background: var(--card-light);
    border: 1px solid var(--edge);
  }
  .card--back {
    top: 444px;
    background: var(--card-dark);
    color: var(--paper-text);
  }
  .front-name {
    position: absolute;
    left: 0;
    width: 572px;
    top: 128px;
    text-align: center;
    font-family: "Open Sans", sans-serif;
    font-weight: 300;
    font-size: 60px;
    letter-spacing: 1px;
    color: var(--ink);
    line-height: 1;
  }
  .front-category {
    position: absolute;
    right: 30px;
    bottom: 16px;
    font-family: "Open Sans", sans-serif;
    font-weight: 400;
    font-size: 22px;
    color: var(--ink);
  }
  .company {
    position: absolute;
    left: 66px;
    top: 66px;
    font-family: "Open Sans", sans-serif;
    font-weight: 400;
    font-size: 33px;
    line-height: 1;
    color: var(--paper-text);
  }
  .person {
    position: absolute;
    left: 67px;
    top: 126px;
    font-family: "Open Sans", sans-serif;
    font-size: 16px;
    line-height: 1.4;
  }
  .person__name { font-weight: 700; }
  .person__role { font-weight: 300; color: var(--soft-text); }
  .contact {
    position: absolute;
    left: 67px;
    top: 191px;
    list-style: none;
    font-family: "Open Sans", sans-serif;
    font-weight: 300;
    font-size: 16px;
    line-height: 22px;
    color: var(--soft-text);
  }
  .back-name {
    position: absolute;
    left: 410px;
    width: 160px;
    top: 106px;
    text-align: center;
    font-family: "Open Sans", sans-serif;
    font-weight: 300;
    font-size: 24px;
    line-height: 1;
    color: var(--paper-text);
  }
  .tagline {
    position: absolute;
    left: 390px;
    width: 200px;
    top: 200px;
    text-align: center;
    font-family: "Kaushan Script", cursive;
    font-size: 26px;
    line-height: 38px;
    color: var(--paper-text);
  }
</style>
</head>
<body>
  <main class="sheet">
    <section class="card card--front" aria-label="Business card front">
      <p class="front-name">FABLE</p>
      <p class="front-category">skincare</p>
    </section>

    <section class="card card--back" aria-label="Business card back">
      <h1 class="company">fable skin care</h1>
      <div class="person">
        <p class="person__name">Name Surname</p>
        <p class="person__role">Designation</p>
      </div>
      <ul class="contact">
        <li>Tel: +00 000 0000</li>
        <li>Email@fableskincare-example.com</li>
        <li>Fax: +00 000 0000</li>
      </ul>
      <p class="back-name">FABLE</p>
      <p class="tagline">Calm Within<br>Glow Without</p>
    </section>
  </main>
</body>
</html>
```